Loyalty card for customers

I would like logo an a section for 10 places, so I can advertise 10th float is free, our business is health and wellness we offer magnesium float, hyperbaric oxygen and infrared sauna

```html
<!DOCTYPE html>
<html lang="en">
<head>
<meta charset="UTF-8">
<title>Tidal Rest – Loyalty Card</title>
<link rel="stylesheet" href="https://fonts.googleapis.com/css2?family=Montserrat:wght@400;500;600;700&family=Oswald:wght@500&family=Fira+Sans:wght@300;400&display=swap">
<style>
  :root {
    --canvas-bg: #f2f2f2;
    --navy-deep: #02202f;
    --navy: #0b3d58;
    --photo-mid: #1a6a92;
    --photo-light: #2f86b3;
    --aqua: #8ed2ef;
    --aqua-light: #bfe9fb;
    --white: #ffffff;
    --ink: #000000;
    --stamp-line: #222222;
  }
  * { box-sizing: border-box; margin: 0; padding: 0; }
  html, body { width: 1200px; height: 702px; overflow: hidden; }
  body {
    background: var(--canvas-bg);
    position: relative;
    font-family: "Montserrat", sans-serif;
  }
  .card {
    position: absolute;
    top: 218px;
    width: 466px;
    height: 266px;
    overflow: hidden;
  }
  /* Front */
  .card-front {
    left: 106px;
    background: linear-gradient(115deg, var(--navy) 0%, #073049 45%, var(--navy-deep) 100%);
  }
  .photo-area {
    position: absolute;
    right: 0;
    top: 0;
    width: 196px;
    height: 231px;
    background: linear-gradient(90deg, rgba(11,61,88,0) 0%, var(--photo-mid) 35%, var(--photo-light) 100%);
  }
  .brand {
    position: absolute;
    left: 36px;
    top: 24px;
    color: var(--aqua);
    font-family: "Montserrat", sans-serif;
    font-weight: 600;
    font-size: 34px;
    line-height: 36px;
    letter-spacing: 6px;
  }
  .card-label {
    position: absolute;
    left: 67px;
    top: 96px;
    color: var(--white);
    font-family: "Oswald", sans-serif;
    font-weight: 500;
    font-size: 15px;
    letter-spacing: 1.5px;
  }
  .services {
    position: absolute;
    left: 46px;
    top: 153px;
    list-style: none;
    color: var(--aqua-light);
    font-family: "Fira Sans", sans-serif;
    font-weight: 400;
    font-size: 15px;
    line-height: 20.5px;
    letter-spacing: 0.3px;
  }
  .services li::before {
    content: "•";
    margin-right: 5px;
    font-size: 12px;
  }
  .contact-bar {
    position: absolute;
    left: 0;
    bottom: 0;
    width: 100%;
    height: 35px;
    background: var(--aqua);
    display: flex;
    align-items: center;
    justify-content: space-between;
    padding: 0 30px 0 42px;
    color: var(--ink);
    font-size: 13px;
  }
  .website { font-weight: 600; letter-spacing: 1px; }
  .social { display: flex; align-items: center; gap: 8px; font-weight: 500; letter-spacing: 0.6px; }
  .social-dot { width: 13px; height: 13px; border-radius: 50%; background: var(--ink); }
  /* Back */
  .card-back {
    left: 633px;
    background: var(--white);
  }
  .stamps { position: absolute; left: 0; top: 0; }
  .offer-bar {
    position: absolute;
    left: 0;
    bottom: 0;
    width: 100%;
    height: 53px;
    background: var(--ink);
    color: var(--white);
    display: flex;
    align-items: center;
    justify-content: center;
    font-size: 14px;
    letter-spacing: 1.6px;
  }
  .offer-bar strong { font-weight: 700; margin-left: 6px; }
  .offer-bar sup {
    font-size: 8px;
    font-weight: 700;
    vertical-align: 6px;
    line-height: 0;
    margin-right: 14px;
  }
</style>
</head>
<body>
  <section class="card card-front">
    <div class="photo-area" role="img" aria-label="Photo area: person floating in an open float pod"></div>
    <div class="brand">Tidal<br>Rest</div>
    <div class="card-label">LOYALTY CARD</div>
    <ul class="services">
      <li>MAGNESIUM FLOAT</li>
      <li>HYPERBARIC OXYGEN</li>
      <li>INFRARED SAUNA</li>
    </ul>
    <div class="contact-bar">
      <span class="website">WWW.YOURSITE.COM</span>
      <span class="social"><span class="social-dot"></span>TidalRest</span>
    </div>
  </section>

  <section class="card card-back">
    <svg class="stamps" width="466" height="213" viewBox="0 0 466 213">
      <g fill="none" stroke="var(--stamp-line)" stroke-width="1.2" stroke-dasharray="3 2.5">
        <circle cx="75" cy="70" r="30"/>
        <circle cx="153" cy="70" r="30"/>
        <circle cx="230" cy="70" r="30"/>
        <circle cx="308" cy="70" r="30"/>
        <circle cx="386" cy="70" r="30"/>
        <circle cx="75" cy="144" r="30"/>
        <circle cx="153" cy="144" r="30"/>
        <circle cx="230" cy="144" r="30"/>
        <circle cx="308" cy="144" r="30"/>
      </g>
      <circle cx="386" cy="144" r="30" fill="var(--ink)"/>
      <text x="386" y="150" text-anchor="middle" fill="var(--white)" font-family="Montserrat, sans-serif" font-weight="700" font-size="16" letter-spacing="1">FREE</text>
    </svg>
    <div class="offer-bar">ENJOY 9 FLOATS &amp; <strong>GET 10</strong><sup>TH</sup><strong>FOR FREE</strong></div>
  </section>
</body>
</html>
```